Stationary Design - KM Facial Plastics

We are looking for a stylish and professional stationary design for a facial plastic surgeon. The stationary design will be for letterhead, business card, appointment cards and envelopes.
The design must be slick and aesthetically pleasing whilst incorporating the style of our logo as attached below.

Target Market(s)

Adults of all ages

Font styles to use
Serif
Script

Requirements
Must have
• Must be an aesthetically pleasing, stylish and professional design that includes the required information in a captivating layout.
• Must also be welcoming with a balanced design and a clean crisp finish.
• Details should include:
• Mr Tobias Wrenfield - Consultant Otolaryngologist & Facial Plastic Surgeon
• Phone: 03 5618 2947
• Fax: 03 5619 7084
• Email: info@kmfacialplastics.example.com.au
• Consulting from: Calderby, Marrowvale, Fenwick, Ashgrove & Kestrel Central
• Appointment Card should include:
• Date, time, fee and location as per the attached example.
• location addresses are:
• 31 Harlow Street Marrowvale Vic 3564
• 148 Brennock Street Calderby Vic 3550
• Level 2, 217 Mabley Street, Fenwick Vic 3076
• Level 4, 263 Denholm Street Melbourne Vic 3000
Should not have
• Clutter

```html
<!DOCTYPE html>
<html lang="en">
<head>
<meta charset="utf-8">
<title>KM Facial Plastics – Stationery Set</title>
<link rel="stylesheet" href="https://fonts.googleapis.com/css2?family=Arimo:wght@400;700&display=swap">
<style>
  :root {
    --backdrop: #b9b9b9;
    --paper: #ffffff;
    --charcoal: #3a3a3a;
    --charcoal-light: #565656;
    --stripe: #a9a9a9;
    --ink: #2b2b2b;
    --ink-soft: #555555;
    --rule: #8a8a8a;
  }
  * { margin: 0; padding: 0; box-sizing: border-box; }
  html, body { width: 1200px; height: 991px; overflow: hidden; }
  body {
    position: relative;
    background: var(--backdrop);
    font-family: "Arimo", Arial, sans-serif;
    color: var(--ink);
  }
  .piece {
    position: absolute;
    background: var(--paper);
    overflow: hidden;
    box-shadow: 0 2px 6px rgba(0,0,0,.25);
  }
  .piece svg.header { position: absolute; left: 0; top: 0; }
  .brand-name {
    position: absolute;
    font-family: "Arimo", Arial, sans-serif;
    font-weight: 400;
    color: var(--ink);
    white-space: nowrap;
    letter-spacing: .03em;
  }
  .small-text { position: absolute; font-size: 4.6px; line-height: 1.35; color: var(--ink-soft); white-space: nowrap; }
  .web b { color: var(--ink); }

  /* Letterhead */
  .letterhead { left: 71px; top: 104px; width: 398px; height: 561px; }
  .letterhead .brand-name { left: 32px; top: 74px; font-size: 11px; }
  .consulting {
    position: absolute; left: 32px; top: 510px; width: 334px;
    display: flex; justify-content: space-between;
    font-size: 5px; letter-spacing: .02em; color: var(--ink-soft);
  }
  .consulting b { color: var(--ink); }
  .letterhead .footer-rule { position: absolute; left: 32px; top: 521px; width: 334px; border-top: .6px solid var(--rule); }
  .letterhead .address { left: 32px; top: 527px; }
  .letterhead .web { right: 32px; top: 533px; }

  /* Folder */
  .folder { left: 508px; top: 90px; width: 432px; height: 575px; border-radius: 4px; }
  .folder .brand-name { left: 0; width: 432px; text-align: center; top: 452px; font-size: 15px; }
  .folder .web { left: 0; width: 432px; text-align: center; top: 535px; font-size: 7px; }

  /* Business cards */
  .card-front { left: 67px; top: 696px; width: 170px; height: 94px; }
  .card-front .name { position: absolute; left: 13px; top: 23px; font-size: 5.6px; font-weight: 700; color: var(--ink); }
  .card-front .title { left: 13px; top: 30px; font-size: 3.4px; }
  .card-front .contacts { left: 13px; top: 60px; font-size: 3.4px; }
  .card-front .url { left: 13px; top: 78px; font-size: 3.4px; }
  .card-front .addr { right: 12px; top: 74px; font-size: 3.4px; text-align: right; }
  .card-front .brand-name { right: 12px; top: 26px; font-size: 5px; }
  .card-back { left: 67px; top: 811px; width: 170px; height: 93px; }
  .card-back .brand-name { left: 0; width: 170px; text-align: center; top: 62px; font-size: 7px; }

  /* DL compliments slip */
  .dl { left: 266px; top: 696px; width: 415px; height: 208px; }
  .dl .brand-name { left: 28px; top: 70px; font-size: 10px; }
  .dl .addr { left: 46px; top: 183px; font-size: 4.8px; }

  /* Envelope */
  .envelope { left: 719px; top: 696px; width: 414px; height: 208px; }
  .envelope .flap-name {
    position: absolute; left: 0; top: 19px; width: 414px; text-align: center;
    font-size: 8px; letter-spacing: .06em; color: var(--paper);
  }
</style>
</head>
<body>

<section class="piece letterhead">
  <svg class="header" width="398" height="70" viewBox="0 0 398 70">
    <path d="M0 0H398V23Q210 28 0 62Z" fill="var(--stripe)"/>
    <path d="M0 0H398V13Q210 18 0 50Z" fill="var(--charcoal)"/>
  </svg>
  <div class="brand-name">KM Facial Plastics</div>
  <div class="consulting">
    <b>CONSULTING FROM:</b><span>|</span><span>CALDERBY</span><span>|</span><span>MARROWVALE</span><span>|</span><span>FENWICK</span><span>|</span><span>ASHGROVE &amp; KESTREL CENTRAL</span>
  </div>
  <div class="footer-rule"></div>
  <div class="small-text address">148 Brennock Street, Calderby, Vic 3987<br>Phone: 03 5618 2947 · Fax: 03 5619 7084 · Email: admin@tidewellclinic.example.com.au</div>
  <div class="small-text web">www.<b>tidewellclinic</b>.example.com.au</div>
</section>

<section class="piece folder">
  <svg class="header" width="432" height="575" viewBox="0 0 432 575">
    <defs>
      <linearGradient id="folderShade" x1="0" y1="0" x2="1" y2="0">
        <stop offset="0" stop-color="var(--charcoal-light)"/>
        <stop offset="1" stop-color="#2f2f2f"/>
      </linearGradient>
      <linearGradient id="folderPaper" x1="0" y1="0" x2="1" y2="1">
        <stop offset="0" stop-color="#ffffff"/>
        <stop offset="1" stop-color="#e6e6e6"/>
      </linearGradient>
    </defs>
    <rect width="432" height="575" fill="url(#folderPaper)"/>
    <path d="M0 0H432V355Q230 362 0 418Z" fill="var(--stripe)"/>
    <path d="M0 0H432V345Q230 352 0 408Z" fill="url(#folderShade)"/>
    <line x1="25" y1="0" x2="25" y2="575" stroke="rgba(0,0,0,.18)" stroke-width="1"/>
  </svg>
  <div class="brand-name">KM Facial Plastics</div>
  <div class="small-text web">www.<b>tidewellclinic</b>.example.com.au</div>
</section>

<section class="piece card-front">
  <svg class="header" width="170" height="20" viewBox="0 0 170 20">
    <path d="M0 0H170V6Q90 8 0 18Z" fill="var(--stripe)"/>
    <path d="M0 0H170V3Q90 5 0 14Z" fill="var(--charcoal)"/>
  </svg>
  <div class="name">Mr Tobias Wrenfield</div>
  <div class="small-text title">Consultant Otolaryngologist<br>&amp; Facial Plastic Surgeon</div>
  <div class="small-text contacts">T: 03 5618 2947<br>F: 03 5619 7084<br>E: admin@tidewellclinic.example.com.au</div>
  <div class="small-text url">www.tidewellclinic.example.com.au</div>
  <div class="small-text addr">148 Brennock Street<br>Calderby, Vic 3987</div>
  <div class="brand-name">KM Facial Plastics</div>
</section>

<section class="piece card-back">
  <svg class="header" width="170" height="55" viewBox="0 0 170 55">
    <path d="M0 0H170V37Q90 40 0 52Z" fill="var(--stripe)"/>
    <path d="M0 0H170V32Q90 35 0 47Z" fill="var(--charcoal)"/>
  </svg>
  <div class="brand-name">KM Facial Plastics</div>
</section>

<section class="piece dl">
  <svg class="header" width="415" height="60" viewBox="0 0 415 60">
    <path d="M0 0H415V22Q220 28 0 57Z" fill="var(--stripe)"/>
    <path d="M0 0H415V15Q220 21 0 49Z" fill="var(--charcoal)"/>
  </svg>
  <div class="brand-name">KM Facial Plastics</div>
  <div class="small-text addr">148 Brennock Street,<br>Calderby, Vic 3987</div>
</section>

<section class="piece envelope">
  <svg class="header" width="414" height="60" viewBox="0 0 414 60">
    <path d="M0 0H414V40Q414 54 400 54H14Q0 54 0 40Z" fill="var(--charcoal)"/>
  </svg>
  <div class="flap-name">KM Facial Plastics</div>
</section>

</body>
</html>
```